Independent Statistical Consultant Business Card

I will be going out as an independent statistical consultant and need a business card. I specialize in data analysis and statistics for health care and public health

I am an Chartered Numeric Analyst from the Northern Quantitative Society. Would like to incorporate that logo into the design

The design should be modern with classic colors, convey accuracy, analytic creativity and responsiveness to client needs.
Updates

The name of the firm will be simply Dale Venturo Applied Statistical Consulting

To all designers, I want to clarify that the QCert logo and the phrase Chartered Numeric Analyst are not the name of the company nor the focus of the card. They are equivalent to being a Lumetra Licensed Technician (LLT) but in the area of statistics The name of the firm will be: Dale Venturo, Applied Statistical Consulting. I look forward to your submissions. Thanks. Dale

Industry/Entity Type

Health

```html
<!DOCTYPE html>
<html lang="en">
<head>
<meta charset="utf-8">
<title>Dale Venturo — Applied Statistical Consulting</title>
<link rel="stylesheet" href="https://fonts.googleapis.com/css2?family=Exo+2:wght@400;600;700&family=Tinos&display=swap">
<style>
  :root {
    --blue: #1e82cf;
    --ink: #2b2b2d;
    --grey: #58585b;
    --placeholder: #e4e6e9;
    --paper: #ffffff;
    --backdrop: #e8e5e0;
  }
  * { margin: 0; padding: 0; box-sizing: border-box; }
  html, body { width: 1200px; height: 818px; overflow: hidden; }
  body {
    background: var(--backdrop);
    font-family: "Exo 2", sans-serif;
    position: relative;
  }
  .card {
    position: absolute;
    top: 254px;
    width: 540px;
    height: 309px;
    background: var(--paper);
    overflow: hidden;
    box-shadow: 0 6px 18px rgba(0,0,0,0.18);
  }
  .card--front { left: 40px; }
  .card--back { left: 620px; }
  .card__art { position: absolute; inset: 0; width: 100%; height: 100%; }
  .card__content { position: absolute; left: 34px; top: 34px; width: 300px; }
  .cert-logo {
    width: 170px;
    height: 54px;
    background: var(--placeholder);
    border-radius: 4px;
  }
  .credential {
    font-family: "Tinos", serif; font-size: 14px; color: var(--grey);
    margin-top: 8px; letter-spacing: 0.3px; white-space: nowrap;
  }
  .credential sup { font-size: 7px; }
  .person { margin-top: 24px; }
  .person__name { font-size: 22px; font-weight: 700; color: var(--blue); line-height: 1; }
  .person__role { font-size: 12px; font-weight: 700; color: var(--grey); margin-top: 3px; }
  .contact { list-style: none; margin-top: 16px; }
  .contact__item {
    display: flex; align-items: center; gap: 10px;
    font-size: 13px; font-weight: 600; color: var(--ink);
    height: 19px; letter-spacing: 0.3px; white-space: nowrap;
  }
  .contact__icon { width: 12px; height: 12px; fill: var(--blue); flex: none; }
</style>
</head>
<body>

<section class="card card--front" aria-label="Business card front">
  <svg class="card__art" viewBox="0 0 540 309" aria-hidden="true">
    <rect x="280" y="0" width="260" height="309" fill="var(--blue)"/>
    <circle cx="262" cy="154" r="240" fill="var(--ink)"/>
    <circle cx="240" cy="154" r="240" fill="var(--paper)"/>
    <rect x="0" y="0" width="260" height="309" fill="var(--paper)"/>
  </svg>
  <div class="card__content">
    <div class="cert-logo" role="img" aria-label="QCert certification logo"></div>
    <p class="credential">Chartered Numeric Analyst<sup>TM</sup></p>
    <div class="person">
      <p class="person__name">Dale Venturo</p>
      <p class="person__role">Applied Statistical Consulting</p>
    </div>
    <ul class="contact">
      <li class="contact__item">
        <svg class="contact__icon" viewBox="0 0 12 12"><path d="M2 0h3l1 3-2 1.2a7 7 0 0 0 3.8 3.8L9 6l3 1v3a2 2 0 0 1-2 2A10 10 0 0 1 0 2a2 2 0 0 1 2-2z"/></svg>
        0012 3456 789
      </li>
      <li class="contact__item">
        <svg class="contact__icon" viewBox="0 0 12 12"><path d="M0 2h12v8H0z"/><path d="M1 3l5 3.5L11 3" fill="none" stroke="#fff" stroke-width="1"/></svg>
        info@youremail.com
      </li>
      <li class="contact__item">
        <svg class="contact__icon" viewBox="0 0 12 12"><circle cx="6" cy="6" r="6"/><path d="M0 6h12M6 0c-3 3-3 9 0 12M6 0c3 3 3 9 0 12" fill="none" stroke="#fff" stroke-width="0.8"/></svg>
        www.yourwebsite.com
      </li>
      <li class="contact__item">
        <svg class="contact__icon" viewBox="0 0 12 12"><path d="M6 0l6 6h-2v6H7.5V8h-3v4H2V6H0z"/></svg>
        Your Adress Inc 2nd Lane, NJ 00000
      </li>
    </ul>
  </div>
</section>

<section class="card card--back" aria-label="Business card back">
  <svg class="card__art" viewBox="0 0 540 309" aria-hidden="true">
    <rect width="540" height="309" fill="var(--blue)"/>
    <circle cx="282" cy="140" r="175" fill="var(--ink)"/>
    <circle cx="258" cy="168" r="175" fill="var(--ink)"/>
    <circle cx="270" cy="154" r="172" fill="var(--paper)"/>
  </svg>
</section>

</body>
</html>
```